Healthy Products Company Needs to Refresh Their Web Image

This is a web relaunch for a company that creates a nutritional supplement made out of Greenlipped Mussels that are native to and grow only in New Zealand. This product is a health superfood which is excellent support for many conditions such as arthritis, heart disease, joint mobility, and healthy lung function, etc. Tovrel Aquaculture is a pioneer in this industry having started in 1967. They have pioneered and are the only company in the business to use cool drying methodology to dry their mussels. This low heat process doesn't degrade nutritional and health giving properties of the mussels. The final design should communicate, cool, healthy, green and natural feeling superimposed on cutting edge technology, and pharmaceutical purity. Natural yet scientific. Also a certain solidity and trustworthiness.
Updates

Hi: The web site name is www.tovrel.com and I would like to have both the psd file and the underlying code.
Thank you.

Target Market(s)

Corporates: Pharmaceutical Companies, Heath Product Companies

Industry/Entity Type

Pharmaceutical

Requirements
Must have
• Currently we have no way to order the product online and we will not be doing this in the current site. However, capability to do that in the future would be nice.
Please see the previous web site for understanding of what the company does. Plese feel free to run with any ideas you may have in layout or content. I have enclosed a new logo for the company. Please make sure you carry the style of the logo throughout the new web site. I don't have any new pictures we can use right now but I will include a background picture you can use for now as a placeholder.

```html
<!DOCTYPE html>
<html lang="en">
<head>
<meta charset="utf-8">
<title>Tovrel Aquaculture Ltd</title>
<link rel="stylesheet" href="https://fonts.googleapis.com/css2?family=Tinos:wght@400;700&family=Oswald:wght@400;500&family=Arimo:wght@400;700&display=swap">
<style>
:root{
  --ink-dark:#0f1c24;
  --brand-blue:#1569c2;
  --brand-green:#13864a;
  --panel-green:#238553;
  --news-blue:#2a7fc6;
  --text-grey:#5b5b5b;
  --page-light:#ebebeb;
  --footer:#2c2c2c;
  --white:#ffffff;
}
*{margin:0;padding:0;box-sizing:border-box}
html,body{width:1200px;height:972px;overflow:hidden}
body{position:relative;font-family:"Arimo",Arial,sans-serif;background:var(--page-light)}
.hero-photo{position:absolute;left:0;top:0;width:1200px;height:686px;
  background:linear-gradient(180deg,#5d95cf 0%,#8fb8de 30%,#5b7d6a 44%,#2b4f3a 50%,#244e8a 58%,#163f80 80%,#0f2f66 100%)}
.top-bar{position:absolute;left:0;top:0;width:1200px;height:56px;background:var(--ink-dark)}
.search{position:absolute;left:216px;top:11px;width:200px;height:25px;background:#16242d;border:1px solid #2d3c45;
  color:#8a969c;font-size:10px;padding:6px 8px;letter-spacing:.5px}
.search svg{position:absolute;right:5px;top:3px}
.social{position:absolute;top:14px;display:flex;gap:10px}
.social span{display:block;width:14px;height:14px;border-radius:50%;background:#c9ced1}
.top-links{position:absolute;top:13px;left:835px;display:flex;gap:28px;font-family:"Tinos",serif;font-size:15px;color:var(--white)}
.main-nav{position:absolute;left:216px;top:45px;width:768px;height:84px;background:linear-gradient(#fff,#ececec);
  border-bottom:6px solid var(--brand-blue);display:flex;box-shadow:0 10px 14px rgba(0,0,0,.35)}
.brand{width:262px;display:flex;align-items:center;gap:8px;padding-left:20px}
.brand-dot{width:22px;height:22px;border-radius:50%;background:var(--brand-green)}
.brand-name{font-family:"Tinos",serif;font-size:22px;color:var(--brand-blue)}
.nav-item{display:flex;align-items:center;padding:0 12px;font-family:"Tinos",serif;font-size:17px;color:var(--brand-green);border-left:1px solid #d9d9d9}
.nav-item.active{background:var(--brand-blue);color:var(--white);padding:0 16px;border:none}
.slide-arrow{position:absolute;top:311px;width:63px;height:99px;background:rgba(20,30,35,.75);display:flex;align-items:center;justify-content:center}
.headline{position:absolute;left:213px;font-family:"Tinos",serif;color:var(--white)}
.headline.lead{top:351px;width:367px;height:46px;background:var(--brand-blue);font-size:36px;padding:2px 12px}
.headline.main{top:397px;width:762px;height:60px;background:var(--brand-green);font-size:46px;padding:2px 12px}
.headline.sub{top:457px;width:367px;height:44px;background:#2b2b2b;font-size:18px;padding:11px 17px}
.video-card{position:absolute;left:207px;top:533px;width:394px;height:118px;background:var(--panel-green);border:2px solid #1a5f3a;box-shadow:0 4px 8px rgba(0,0,0,.4)}
.video-thumb{position:absolute;left:12px;top:12px;width:135px;height:87px;background:linear-gradient(#fff,#e8e8e8);display:flex;align-items:center;justify-content:center}
.video-title{position:absolute;left:159px;top:11px;font-family:"Oswald",sans-serif;font-size:18px;line-height:23px;color:var(--white)}
.video-text{position:absolute;left:159px;top:64px;width:225px;font-size:10px;line-height:12px;color:#e3f1e8}
.map-card{position:absolute;left:609px;top:533px;width:374px;height:118px;background:#1b55a0;border:2px solid #143e76;padding:5px;box-shadow:0 4px 8px rgba(0,0,0,.4)}
.map-fill{width:100%;height:100%;background:linear-gradient(90deg,#c8d7a0,#a9c58f 55%,#8fb8dc 70%,#e9c070)}
.intro{position:absolute;left:209px;top:703px}
.intro-title{font-family:"Tinos",serif;font-size:37px;color:var(--brand-blue);white-space:nowrap}
.intro-title .lead-word{color:var(--brand-green)}
.intro-title sup{font-size:18px}
.intro-copy{position:absolute;left:209px;top:759px;width:320px;font-size:9.7px;line-height:12px;color:var(--text-grey)}
.intro-copy p+p{margin-top:12px}
.farm-photo{position:absolute;left:537px;top:748px;width:184px;height:117px;border:2px solid #cfcfcf;background:linear-gradient(180deg,#4d90d2 0%,#7ab0e0 35%,#2d5a3c 42%,#0f3d73 60%,#0b2a55 100%)}
.news{position:absolute;left:740px;top:677px;width:243px;height:181px;background:linear-gradient(#2f8ad1,#236eb4);border:2px solid #1b5c98;color:var(--white);padding:9px 9px;box-shadow:0 4px 8px rgba(0,0,0,.3)}
.news h2{font-family:"Oswald",sans-serif;font-weight:500;font-size:26px;line-height:30px;margin-bottom:10px}
.news-item{display:flex;gap:10px;padding-bottom:7px}
.news-item+.news-item{border-top:1px dashed #9cc6ea;padding-top:7px}
.date{width:37px;height:35px;border:2px solid var(--white);text-align:center;font-family:"Oswald",sans-serif;font-size:16px;line-height:17px}
.date small{display:block;font-size:7px;line-height:9px}
.news-item b{font-size:11px;display:block}
.news-item p{font-size:10px;line-height:12px}
.footer{position:absolute;left:0;top:896px;width:1200px;height:76px;background:linear-gradient(#383838,#222)}
.footer .brand{position:absolute;left:209px;top:21px;padding:0}
.footer .brand-name{font-size:21px}
.footer-links{position:absolute;left:480px;top:22px;display:flex;font-size:10px;color:var(--white)}
.footer-links span{padding:0 14px;border-left:1px solid #ccc}
.footer-links span:first-child{padding-left:0;border:none}
.copyright{position:absolute;left:480px;top:42px;font-size:10px;color:#ddd}
</style>
</head>
<body>
<div class="hero-photo" role="img" aria-label="Coastal bay with green hills, mountains and a city skyline under blue sky"></div>

<header class="top-bar">
  <div class="search">SEARCH
    <svg width="18" height="18" viewBox="0 0 18 18"><circle cx="7" cy="7" r="5" fill="none" stroke="#ccc" stroke-width="2"/><line x1="11" y1="11" x2="16" y2="16" stroke="#ccc" stroke-width="2.5"/></svg>
  </div>
  <div class="social" style="left:685px"><span></span><span></span><span></span><span></span><span></span></div>
  <nav class="top-links"><span>Contact Us</span><span>Site Map</span></nav>
</header>

<nav class="main-nav">
  <div class="brand"><span class="brand-dot"></span><span class="brand-name">Tovrel Aquaculture Ltd</span></div>
  <div class="nav-item active">Home</div>
  <div class="nav-item">The Tovrel Story</div>
  <div class="nav-item">Mussel Powder</div>
  <div class="nav-item">Background Information</div>
</nav>

<div class="slide-arrow" style="left:0"><svg width="26" height="34"><polygon points="24,2 24,32 4,17" fill="#ddd"/></svg></div>
<div class="slide-arrow" style="left:1137px"><svg width="26" height="34"><polygon points="2,2 2,32 22,17" fill="#ddd"/></svg></div>

<h1 class="headline lead">Fresh Powder Of</h1>
<div class="headline main">Natural Foods For The Health Foods</div>
<div class="headline sub">Supplements, and Food Ingredients industries</div>

<section class="video-card">
  <div class="video-thumb"><svg width="30" height="20"><rect width="30" height="20" rx="4" fill="#222"/><polygon points="12,5 12,15 20,10" fill="#fff"/></svg></div>
  <div class="video-title">Integer sed lorem enim<br>non nunc nemalesuada</div>
  <p class="video-text">Donec consequat malesuada enim id tincidunt. Vivamus justo ligula, tempor ut lobortis sit amet, pulvinar posuere elit.</p>
</section>
<section class="map-card"><div class="map-fill" role="img" aria-label="Map of the coastal region and its farming bays"></div></section>

<h2 class="intro intro-title"><span class="lead-word">Tovrel<sup>®</sup></span> Aquaculture Ltd</h2>
<div class="intro-copy">
  <p>Tovrel® Aquaculture Ltd. produces a fresh powder of natural foods for the Health Foods, Supplements, and Food Ingredients industries. The main activity is the processing of the New Zealand CoastgreenTM Mussel into a fine, dense powder which retains the highest quality of bioactive nutrients from the Sea - "The Cradle of Life."</p>
  <p>The quality of our products are the best in their category due to careful selection of mussels grown nearby, and the "one step, short time," spray-drying technique called the Tovrel® Process.</p>
</div>
<div class="farm-photo" role="img" aria-label="Mussel farm lines floating on a calm bay"></div>

<aside class="news">
  <h2>LATEST NEWS</h2>
  <div class="news-item"><div class="date">20<small>MAR</small></div><div><b>Adipiscing elit, Lorem ipsum</b><p>Lorem ipsum dolor sit amet, consectetuer sed diam.adipiscing elit, Lorem ipsum dolor sit amet,</p></div></div>
  <div class="news-item"><div class="date">20<small>MAR</small></div><div><b>Adipiscing elit, Lorem ipsum</b><p>Lorem ipsum dolor sit amet, consectetuer sed diam.adipiscing elit, Lorem ipsum dolor sit amet,</p></div></div>
</aside>

<footer class="footer">
  <div class="brand"><span class="brand-dot"></span><span class="brand-name">Tovrel Aquaculture Ltd</span></div>
  <nav class="footer-links"><span>HOME</span><span>PRIVACY POLICY</span><span>CONTACT US</span><span>SITE MAP</span></nav>
  <div class="copyright">© 2013 Tovrel Aquaculture All Rights Reserved</div>
  <div class="social" style="left:826px;top:29px;gap:14px"><span></span><span></span><span></span><span></span><span></span></div>
</footer>
</body>
</html>
```